User Interface Design for new Team Management App

We're developing a new app with a unique, two part, user interface. The artistic section of our UI is complete, we now need the functional part completed. The functional part will include menus, inputting data, scrolling and etc. We have our own developers and coders, so no need to worry about that.

The contest:
The artist we decide to work with will submit a design which will be their vision for the entirety of the project. See the brief for more information, it is attached.

Points to remember:
-We like artists to submit fast
-Please follow the brief
-Please show examples of other UI work you have completed in the past
-We like people who communicate promptly, openly and professionally.

Thank you, and good luck.

Industry/Entity Type

Management

```html
<!DOCTYPE html>
<html lang="en">
<head>
<meta charset="utf-8">
<title>Team App – Leadership Card Screen</title>
<link rel="stylesheet" href="https://fonts.googleapis.com/css2?family=Lato:ital,wght@0,400;0,700;1,400;1,700&display=swap">
<style>
  :root {
    --stage-bg: #ece4f8;
    --card-white: #ffffff;
    --band-pink: #ebd3d6;
    --band-pink-light: #f6e9ea;
    --accent-red: #d25f5e;
    --quote-red: #d6454a;
    --text-ink: #1f1f1f;
    --close-grey: #c9c0c2;
    --wash-blue: #8e90c4;
    --wash-purple: #a0739a;
    --wash-green: #8cc08f;
    --wash-teal: #6e9fc0;
    --wash-yellow: #e7d38a;
    --wash-olive: #cdbf86;
  }
  * { box-sizing: border-box; margin: 0; padding: 0; }
  html, body {
    width: 1200px; height: 1000px; overflow: hidden;
    background: var(--stage-bg);
    font-family: "Lato", Helvetica, Arial, sans-serif;
  }
  .app-screen {
    position: absolute; left: 350px; top: 56px;
    width: 500px; height: 888px;
    overflow: hidden;
    background: #f2efe9;
  }
  .artistic-background {
    position: absolute; inset: 0;
    background:
      radial-gradient(ellipse 60% 30% at 80% 8%, var(--wash-blue) 0%, transparent 70%),
      radial-gradient(ellipse 40% 30% at 100% 20%, var(--wash-purple) 0%, transparent 70%),
      radial-gradient(ellipse 45% 30% at 100% 62%, var(--wash-green) 0%, transparent 70%),
      radial-gradient(ellipse 60% 25% at 75% 92%, var(--wash-teal) 0%, transparent 70%),
      radial-gradient(ellipse 40% 45% at 0% 45%, var(--wash-olive) 0%, transparent 70%),
      radial-gradient(ellipse 45% 35% at 5% 85%, var(--wash-yellow) 0%, transparent 70%),
      #efece6;
  }
  .info-card {
    position: absolute; left: 22px; top: 34px;
    width: 456px; height: 700px;
    background: var(--card-white);
    border-radius: 16px;
    box-shadow: 0 2px 10px rgba(0,0,0,0.12);
    overflow: hidden;
  }
  .card-band {
    position: absolute; left: 0; top: 22px;
    width: 100%; height: 118px;
    background: linear-gradient(90deg, var(--band-pink) 0%, var(--band-pink-light) 45%, var(--band-pink) 100%);
  }
  .portrait-medallion {
    position: absolute; left: 50%; top: 10px;
    width: 96px; height: 96px;
    margin-left: -48px;
    border-radius: 50%;
    background: radial-gradient(circle, #4d6f8a 0%, #7fa6c2 45%, #f1dcdd 60%, #e6c3c6 100%);
  }
  .close-button {
    position: absolute; right: 16px; top: 46px;
    width: 26px; height: 26px;
  }
  .card-quote {
    position: absolute; left: 36px; right: 36px; top: 152px;
    color: var(--quote-red);
    font-style: italic; font-weight: 700;
    font-size: 17px; line-height: 1.3;
    text-align: center;
  }
  .card-body {
    position: absolute; left: 40px; right: 36px; top: 212px;
    color: var(--text-ink);
    font-size: 18px; line-height: 1.38;
    text-align: justify;
  }
  .card-body p { text-indent: 1.4em; margin-bottom: 14px; }
  .card-rule {
    position: absolute; left: 22px; right: 22px; top: 600px;
    height: 6px;
    border-top: 1.5px solid var(--accent-red);
    border-bottom: 1.5px solid var(--accent-red);
    opacity: 0.6;
  }
  .next-button {
    position: absolute; left: 12px; right: 12px; top: 716px;
    height: 132px;
    background: var(--accent-red);
    border-radius: 8px;
    color: #fff;
    font-size: 28px; letter-spacing: 1px;
    display: flex; align-items: center; justify-content: center;
    border: none;
  }
</style>
</head>
<body>
  <main class="app-screen">
    <div class="artistic-background" role="img" aria-label="Soft watercolour wash in blue, purple, green, teal and yellow"></div>

    <article class="info-card">
      <div class="card-band">
        <div class="portrait-medallion" role="img" aria-label="Portrait of a historical leader in an ornamental frame"></div>
        <svg class="close-button" viewBox="0 0 26 26" aria-label="Close">
          <path d="M3 3 L23 23 M23 3 L3 23" stroke="var(--close-grey)" stroke-width="3" stroke-linecap="round"/>
        </svg>
      </div>

      <p class="card-quote">‘If your actions inspire others to dream more, learn more, do more and become more, you are a leader’</p>

      <div class="card-body">
        <p>A leader must have a mission and a clear vision in their mind to inspire their team. They must know their team well, they must understand them. They then need to set out a series of small steps in order to guide their team toward achieving their mission.</p>
        <p>At the same time they’re doing this they must recognize and show appreciation to everyone and keep communucation strong. Then there’s everything else..</p>
      </div>

      <div class="card-rule"></div>
    </article>

    <button class="next-button">NEXT</button>
  </main>
</body>
</html>
```